Redesign This Psychology Website

We would like a slight redesign of this successful psychology (relationship counselling) website:

www.TheWillowNook.com.au

We are updating the website, and we'd like a slight refresh of the design and style.

Please keep to very similar colours, and use the same logo. We're looking for around 10 page templates, however the main one is the home page.

Keep in mind, this website already converts quite well, so we want a new, fresh design in keeping with this one. Please don't bother designing something too extremely different.

thanks :)

Target Market(s)

couples who are looking for relationship counselling. Men and women, 25 - 70, across Australia

Industry/Entity Type

Psychology

Number of Pages Required

5+ page

Font styles to use
Sans Serif

Colors
87cfc6
b7a5cd
ec1f27
ffffff
cee9f5

Requirements
Must have
• a similar look to the current design, just looking for a slight refresh.
• Search bar
• Areas for lots of photos
• same logo
• lots of content areas
Nice to have
• great content areas, where we can display a lot of content and our areas.
Should not have
• no colors like orange, etc.
• should not have a totally different feel.

```html
<!DOCTYPE html>
<html lang="en">
<head>
<meta charset="utf-8">
<title>Willow Nook – Relationship Counselling</title>
<link href="https://fonts.googleapis.com/css2?family=Raleway:wght@400;500;600;700&family=Open+Sans:wght@400;600&display=swap" rel="stylesheet">
<style>
:root{
  --teal:#87cfc6;
  --teal-dark:#5fb9ae;
  --red:#ec1f27;
  --coral:#f0565b;
  --ink:#2b2b2b;
  --muted:#8a8a8a;
  --line:#e6e6e6;
  --white:#ffffff;
  --sky:#cee9f5;
  --lilac:#b7a5cd;
}
*{box-sizing:border-box;margin:0;padding:0}
html,body{width:1200px;height:3279px;overflow:hidden;background:var(--white)}
body{font-family:"Open Sans",Arial,sans-serif;color:var(--ink);position:relative}
.abs{position:absolute}
a{color:inherit;text-decoration:none}
h1,h2,h3,.heading{font-family:"Raleway",Arial,sans-serif}

/* top bar */
.topbar{top:0;left:0;width:1200px;height:40px;border-bottom:1px solid var(--line)}
.topbar .welcome{left:160px;top:13px;font-size:11px;letter-spacing:1px;color:var(--muted);text-transform:uppercase}
.topbar .social{right:160px;top:0;display:flex;height:40px}
.topbar .social span{width:35px;height:40px;border-left:1px solid var(--line);display:flex;align-items:center;justify-content:center}
.topbar .social span:last-child{border-right:1px solid var(--line)}
.topbar .social i{width:8px;height:8px;border-radius:50%;background:#b5b5b5;display:block}

/* header */
.header{top:40px;left:0;width:1200px;height:87px}
.brand{left:160px;top:18px;display:flex;align-items:center;gap:10px}
.brand .mark{width:30px;height:30px;border-radius:50%;background:var(--teal)}
.brand .name{font-family:"Raleway",sans-serif;font-weight:500;font-size:31px;color:var(--teal-dark);line-height:1}
.brand-tag{left:200px;top:58px;font-size:12px;color:var(--teal-dark);font-family:"Raleway",sans-serif;font-weight:600}
.contact-item{top:32px;font-size:13px;display:flex;align-items:center;gap:8px;text-transform:uppercase;color:var(--ink)}
.btn-red{background:var(--red);color:var(--white);font-weight:600;font-size:13px;text-transform:uppercase;display:flex;align-items:center;justify-content:center;font-family:"Raleway",sans-serif}

/* nav */
.nav{top:127px;left:0;width:1200px;height:44px;background:var(--teal)}
.nav ul{position:absolute;left:177px;top:0;height:44px;display:flex;list-style:none;align-items:center;gap:26px}
.nav li{color:var(--white);font-size:12.5px;font-weight:600;font-family:"Raleway",sans-serif;text-transform:uppercase}
.nav .search{right:160px;top:0;width:50px;height:44px;background:var(--red);display:flex;align-items:center;justify-content:center}

/* hero */
.hero{top:171px;left:0;width:1200px;height:448px;background:linear-gradient(100deg,#8c9aa0 0%,#a9b7bb 35%,#c9b39d 65%,#e5d6c4 100%)}
.hero-title{left:170px;top:315px;font-size:38px;font-weight:700;color:var(--white);letter-spacing:1px;font-family:"Raleway",sans-serif}
.hero-sub{left:172px;top:368px;font-size:14px;color:var(--white)}
.hero-btn{left:172px;top:413px;width:92px;height:31px}

/* about */
.about{top:619px;left:0;width:1200px;height:216px;background:var(--teal)}
.about .photo{left:285px;top:23px;width:160px;height:160px;border-radius:50%;background:linear-gradient(160deg,#f2dcc4,#d9a57d);border:4px solid rgba(255,255,255,.6)}
.about .kicker{left:462px;top:36px;font-size:9px;color:var(--white);text-transform:uppercase;letter-spacing:1px;font-weight:600}
.about h2{position:absolute;left:460px;top:50px;font-size:33px;font-weight:400;color:var(--white)}
.about p{position:absolute;left:462px;top:106px;width:470px;font-size:13px;line-height:23px;color:var(--white)}

/* section titles */
.sec-title{width:1200px;left:0;text-align:center;font-size:38px;font-weight:500;font-family:"Raleway",sans-serif;color:var(--ink)}
.sec-rule{left:572px;width:56px;height:2px;background:var(--red)}

/* services */
.service{top:964px;width:220px;text-align:center}
.service .circle{width:136px;height:136px;border-radius:50%;margin:0 auto}
.service h3{font-size:13.5px;font-weight:600;margin-top:31px;color:var(--ink)}
.service p{font-size:10.5px;line-height:16px;color:var(--muted);margin:18px auto 0;width:170px}
.learn{color:var(--red);font-size:10.5px;font-weight:600;display:block;margin-top:14px}

/* psychologists */
.split-photo{top:1298px;left:0;width:494px;height:350px;background:linear-gradient(120deg,#7f9167 0%,#b6c290 45%,#d8c7b2 100%)}
.split{top:1298px;left:494px;width:706px;height:350px;background:var(--coral)}
.split h2{position:absolute;left:33px;top:40px;font-size:23px;font-weight:600;color:var(--white)}
.split ul{position:absolute;top:94px;list-style:none}
.split li{color:var(--white);font-size:11.5px;font-weight:600;height:22.4px;display:flex;align-items:center;gap:9px;font-family:"Raleway",sans-serif}

/* blogs */
.blog{top:1773px;width:250px;text-align:center}
.blog .thumb{height:142px}
.blog .date{font-size:9px;color:var(--muted);margin-top:26px;text-transform:uppercase}
.blog h3{font-size:15px;font-weight:500;line-height:20px;margin-top:11px;color:var(--ink)}
.blog p{font-size:10.5px;line-height:16px;color:var(--muted);margin:25px auto 0;width:210px}

/* gallery */
.gallery{top:2190px;left:0;width:1200px;height:396px;background:var(--teal)}
.gallery .strip{left:210px;top:151px;width:785px;height:158px;display:flex}
.gallery .strip div{flex:1}
.arrow{top:215px}

/* testimonial */
.testimonial{top:2586px;left:0;width:1200px;height:370px;background:linear-gradient(90deg,#5e5a57 0%,#7d7874 40%,#8c8985 70%,#6c6a68 100%)}
.testimonial .avatar{left:556px;top:68px;width:88px;height:88px;border-radius:50%;background:linear-gradient(160deg,#e8cfb8,#a7765a);border:3px solid rgba(255,255,255,.7)}
.testimonial .quote{left:300px;top:178px;width:600px;text-align:center;color:var(--white);font-size:13px;line-height:23px}
.testimonial .who{left:0;width:1200px;top:233px;text-align:center;color:var(--white);font-size:11px}
.dots{left:580px;top:278px;display:flex;gap:7px}
.dots i{width:8px;height:8px;border-radius:50%;border:1px solid var(--white);display:block}
.dots i.on{background:var(--white)}

/* footer */
.footer{top:2956px;left:0;width:1200px;height:281px}
.footer .fbrand{left:160px;top:56px}
.footer .about-text{left:160px;top:118px;width:215px;font-size:11px;line-height:18px;color:var(--muted)}
.footer h4{position:absolute;top:60px;font-family:"Raleway",sans-serif;font-size:16px;font-weight:600;color:var(--ink)}
.footer h4::after{content:"";display:block;width:40px;height:2px;background:var(--red);margin-top:6px}
.footer .links{top:110px;font-size:11px;line-height:22px;color:var(--muted);list-style:none}
.field{left:748px;top:118px;width:220px;height:33px;background:#eeeeee;font-size:11px;color:#aaa;padding:9px 12px}
.signup{left:968px;top:118px;width:66px;height:33px;font-size:11px}
.fsocial{left:748px;top:174px;display:flex;gap:5px}
.fsocial i{width:20px;height:20px;border-radius:50%;border:1.5px solid var(--teal-dark);display:block}
.copyright{top:3237px;left:0;width:1200px;height:42px;background:var(--red);color:var(--white);font-size:11px;font-weight:600;display:flex;align-items:center;justify-content:center}
</style>
</head>
<body>

<!-- Top bar -->
<div class="abs topbar">
  <div class="abs welcome">Welcome to Willow Nook</div>
  <div class="abs social"><span><i></i></span><span><i></i></span><span><i></i></span><span><i></i></span></div>
</div>

<!-- Header -->
<header class="abs header">
  <div class="abs brand"><span class="mark"></span><span class="name">Willow Nook</span></div>
  <div class="abs brand-tag">helping you create loving relationships</div>
  <div class="abs contact-item" style="left:608px">
    <svg width="12" height="12" viewBox="0 0 12 12"><circle cx="6" cy="6" r="6" fill="#ec1f27"/><path d="M6 3v3l2 1.5" stroke="#fff" stroke-width="1.3" fill="none"/></svg>
    Book an appointment
  </div>
  <div class="abs contact-item" style="left:810px">
    <svg width="12" height="12" viewBox="0 0 24 24"><path fill="#ec1f27" d="M6.6 10.8a15 15 0 0 0 6.6 6.6l2.2-2.2a1 1 0 0 1 1-.25 11.4 11.4 0 0 0 3.6.57 1 1 0 0 1 1 1V20a1 1 0 0 1-1 1A17 17 0 0 1 3 4a1 1 0 0 1 1-1h3.5a1 1 0 0 1 1 1c0 1.25.2 2.45.57 3.6a1 1 0 0 1-.25 1z"/></svg>
    1300 475 218
  </div>
  <div class="abs btn-red" style="left:912px;top:26px;width:128px;height:32px">View Locations</div>
</header>

<!-- Navigation -->
<nav class="abs nav">
  <ul>
    <li>Home</li><li>About</li><li>Blog</li><li>Counselling Type ⌄</li><li>Relationship Counselling ⌄</li><li>Quizzes</li><li>F.A.Q'S</li><li>Contact</li>
  </ul>
  <div class="abs search">
    <svg width="20" height="20" viewBox="0 0 20 20"><circle cx="8" cy="8" r="6" stroke="#fff" stroke-width="2" fill="none"/><path d="M12.5 12.5L18 18" stroke="#fff" stroke-width="2.2"/></svg>
  </div>
</nav>

<!-- Hero -->
<section class="abs hero" role="img" aria-label="Photo of a smiling couple embracing"></section>
<h1 class="abs hero-title">IMPROVE YOUR LIFE</h1>
<div class="abs hero-sub">Relate To Each Other from the best in you ...</div>
<div class="abs btn-red hero-btn">Read More</div>

<!-- About -->
<section class="abs about">
  <div class="abs photo" role="img" aria-label="Portrait of the psychologist"></div>
  <div class="abs kicker">About Me</div>
  <h2>Hello! I'm Clara Benton</h2>
  <p>I am a psychologist and my goal is to partner with you to enhance the quality of your life. Whether you are dealing with something specific or are seeking increased satisfaction and balance in life, I'm here to help.</p>
</section>

<!-- Services -->
<h2 class="abs sec-title" style="top:882px">How I Can Help You</h2>
<div class="abs sec-rule" style="top:930px"></div>

<div class="abs service" style="left:163px">
  <div class="circle" role="img" aria-label="Photo of a happy couple" style="background:linear-gradient(150deg,#e3b58e,#8f5f44)"></div>
  <h3>Relationship Counselling</h3>
  <p>Rebuild trust and closeness with caring, practical support for couples.</p>
  <span class="learn">Learn More &gt;&gt;</span>
</div>
<div class="abs service" style="left:382px">
  <div class="circle" role="img" aria-label="Photo of a couple in bed" style="background:linear-gradient(150deg,#f0ece8,#b9aca2)"></div>
  <h3>Sex Therapy &nbsp;Counselling</h3>
  <p>Explore intimacy concerns safely in a calm, private setting today.</p>
  <span class="learn">Learn More &gt;&gt;</span>
</div>
<div class="abs service" style="left:611px">
  <div class="circle" role="img" aria-label="Photo of an angry man shouting" style="background:linear-gradient(150deg,#9a9a9a,#4c4440)"></div>
  <h3>Anger Management Counselling</h3>
  <p>Learn tools to manage anger and respond with calm clarity.</p>
  <span class="learn">Learn More &gt;&gt;</span>
</div>
<div class="abs service" style="left:826px">
  <div class="circle" role="img" aria-label="Photo of a woman looking in a mirror" style="background:linear-gradient(150deg,#d9dde3,#a88a74)"></div>
  <h3>Narcissism Counselling</h3>
  <p>Understand difficult patterns and set healthy boundaries with support.</p>
  <span class="learn">Learn More &gt;&gt;</span>
</div>

<!-- Psychologists -->
<div class="abs split-photo" role="img" aria-label="Photo of a family playing outdoors"></div>
<section class="abs split">
  <h2>Our Willow Nook Relationship Psychologists</h2>
  <ul style="left:37px">
    <li><svg width="11" height="9" viewBox="0 0 11 9"><path d="M1 4.5l3 3L10 1" stroke="#fff" stroke-width="2" fill="none"/></svg>Affairs</li>
    <li><svg width="11" height="9" viewBox="0 0 11 9"><path d="M1 4.5l3 3L10 1" stroke="#fff" stroke-width="2" fill="none"/></svg>Controlling behaviour</li>
    <li><svg width="11" height="9" viewBox="0 0 11 9"><path d="M1 4.5l3 3L10 1" stroke="#fff" stroke-width="2" fill="none"/></svg>Verbal abuse</li>
    <li><svg width="11" height="9" viewBox="0 0 11 9"><path d="M1 4.5l3 3L10 1" stroke="#fff" stroke-width="2" fill="none"/></svg>Imbalance of power</li>
    <li><svg width="11" height="9" viewBox="0 0 11 9"><path d="M1 4.5l3 3L10 1" stroke="#fff" stroke-width="2" fill="none"/></svg>Lack of intimacy</li>
    <li><svg width="11" height="9" viewBox="0 0 11 9"><path d="M1 4.5l3 3L10 1" stroke="#fff" stroke-width="2" fill="none"/></svg>Poor communication</li>
    <li><svg width="11" height="9" viewBox="0 0 11 9"><path d="M1 4.5l3 3L10 1" stroke="#fff" stroke-width="2" fill="none"/></svg>Loss of love</li>
    <li><svg width="11" height="9" viewBox="0 0 11 9"><path d="M1 4.5l3 3L10 1" stroke="#fff" stroke-width="2" fill="none"/></svg>Relationship neglect</li>
    <li><svg width="11" height="9" viewBox="0 0 11 9"><path d="M1 4.5l3 3L10 1" stroke="#fff" stroke-width="2" fill="none"/></svg>Sexual problems</li>
  </ul>
  <ul style="left:289px">
    <li><svg width="11" height="9" viewBox="0 0 11 9"><path d="M1 4.5l3 3L10 1" stroke="#fff" stroke-width="2" fill="none"/></svg>Problems from childhood</li>
    <li><svg width="11" height="9" viewBox="0 0 11 9"><path d="M1 4.5l3 3L10 1" stroke="#fff" stroke-width="2" fill="none"/></svg>Problems with parenting your children</li>
    <li><svg width="11" height="9" viewBox="0 0 11 9"><path d="M1 4.5l3 3L10 1" stroke="#fff" stroke-width="2" fill="none"/></svg>Step children and in-laws</li>
    <li><svg width="11" height="9" viewBox="0 0 11 9"><path d="M1 4.5l3 3L10 1" stroke="#fff" stroke-width="2" fill="none"/></svg>All forms of family problems</li>
    <li><svg width="11" height="9" viewBox="0 0 11 9"><path d="M1 4.5l3 3L10 1" stroke="#fff" stroke-width="2" fill="none"/></svg>Anger management problems</li>
    <li><svg width="11" height="9" viewBox="0 0 11 9"><path d="M1 4.5l3 3L10 1" stroke="#fff" stroke-width="2" fill="none"/></svg>Porn addiction problems</li>
    <li><svg width="11" height="9" viewBox="0 0 11 9"><path d="M1 4.5l3 3L10 1" stroke="#fff" stroke-width="2" fill="none"/></svg>Pre-marriage programs</li>
    <li><svg width="11" height="9" viewBox="0 0 11 9"><path d="M1 4.5l3 3L10 1" stroke="#fff" stroke-width="2" fill="none"/></svg>Narcissism problems</li>
  </ul>
</section>

<!-- Blogs -->
<h2 class="abs sec-title" style="top:1686px">Recent Blogs</h2>
<div class="abs sec-rule" style="top:1734px"></div>

<article class="abs blog" style="left:210px">
  <div class="thumb" role="img" aria-label="Photo of a therapist taking notes" style="background:linear-gradient(135deg,#c9c9c9,#eeeeee)"></div>
  <div class="date">March 7, 2016</div>
  <h3>Cognitive Behavioral Therapy<br>for Insomnia</h3>
  <p>Simple evidence based steps to settle your mind, rest deeply and wake up refreshed each day.</p>
  <span class="learn">Learn More &gt;&gt;</span>
</article>
<article class="abs blog" style="left:478px">
  <div class="thumb" role="img" aria-label="Photo of a couple in a counselling session" style="background:linear-gradient(135deg,#e9e2da,#b7a79a)"></div>
  <div class="date">March 7, 2016</div>
  <h3>Family Therapy and Marriage<br>Counseling</h3>
  <p>How working together with a therapist can help partners listen, heal and plan a shared future.</p>
  <span class="learn">Learn More &gt;&gt;</span>
</article>
<article class="abs blog" style="left:745px">
  <div class="thumb" role="img" aria-label="Photo of hands writing on a clipboard" style="background:linear-gradient(135deg,#f1eeeb,#c8bdb3)"></div>
  <div class="date">March 7, 2016</div>
  <h3>Six Important Rules for<br>Parenting Teenagers</h3>
  <p>Clear, kind boundaries help teenagers feel safe while they learn to make their own choices.</p>
  <span class="learn">Learn More &gt;&gt;</span>
</article>

<!-- Gallery -->
<section class="abs gallery">
  <h2 class="abs sec-title" style="top:42px;color:#fff">My Gallery</h2>
  <div class="abs sec-rule" style="top:92px;background:#fff"></div>
  <div class="abs strip">
    <div role="img" aria-label="Photo of a smiling couple" style="background:linear-gradient(150deg,#d7a47f,#7b5441)"></div>
    <div role="img" aria-label="Portrait of a smiling woman" style="background:linear-gradient(150deg,#f1e7de,#c99f82)"></div>
    <div role="img" aria-label="Portrait of a smiling man" style="background:linear-gradient(150deg,#e6e3e0,#b99077)"></div>
    <div role="img" aria-label="Photo of a counselling session" style="background:linear-gradient(150deg,#cfc9c2,#7e6e63)"></div>
    <div role="img" aria-label="Photo of a smiling couple" style="background:linear-gradient(150deg,#efe9e2,#c08e6b)"></div>
  </div>
  <svg class="abs arrow" style="left:145px" width="16" height="24" viewBox="0 0 16 24"><path d="M13 2L3 12l10 10" stroke="#fff" stroke-width="3" fill="none"/></svg>
  <svg class="abs arrow" style="left:1040px" width="16" height="24" viewBox="0 0 16 24"><path d="M3 2l10 10L3 22" stroke="#fff" stroke-width="3" fill="none"/></svg>
</section>

<!-- Testimonial -->
<section class="abs testimonial" role="img" aria-label="Background photo of a thoughtful woman">
  <div class="abs avatar" role="img" aria-label="Client portrait"></div>
  <p class="abs quote">I recommend this doctor to all my friends. With the help of your books and blog articles I was able to find answers to many questions. It feels great to know what you want in life.</p>
  <div class="abs who"><strong>Mia Collins</strong>, student</div>
  <div class="abs dots"><i></i><i></i><i class="on"></i></div>
</section>

<!-- Footer -->
<footer class="abs footer">
  <div class="abs brand fbrand" style="top:54px"><span class="mark"></span><span class="name">Willow Nook</span></div>
  <div class="abs brand-tag" style="top:92px">helping you create loving relationships</div>
  <p class="abs about-text">Emphasis on gender differences and a scientific and empirical approach, while the more therapeutic scientific orientation is more closely aligned...</p>

  <h4 style="left:455px">Important Links</h4>
  <ul class="abs links" style="left:455px">
    <li>Home</li><li>About</li><li>Blog</li><li>Counselling Type</li><li>Relationship Counselling</li>
  </ul>
  <ul class="abs links" style="left:610px">
    <li>Quizzes</li><li>F.A.Q'S</li><li>Contact</li>
  </ul>

  <h4 style="left:748px">Newsletter Signup</h4>
  <div class="abs field">Email</div>
  <div class="abs btn-red signup">Sign Up</div>
  <div class="abs fsocial"><i></i><i></i><i></i><i></i></div>
</footer>

<div class="abs copyright">The Willow Nook © 2016 All Rights Reserved Terms of Use and Privacy Policy</div>

</body>
</html>
```